IT Company based on Biology Business Needs a PowerPoint Design

We need a powerpoint design for a new company called 'Vast KELP'. We develop the machine learning solutions especially focused on deep learning algorithms for biology industry. Our initial product is a vision detection on biological images to help doctors diagnose the symptoms. We would like to see designs that use the color green.

Industry/Entity Type

Biotechnology

Requirements
Nice to have
• Lots of slide templates with company logo's look and feel

```html
<!DOCTYPE html>
<html lang="en">
<head>
<meta charset="utf-8">
<title>Vast KELP – Content Slide</title>
<link rel="stylesheet" href="https://fonts.googleapis.com/css2?family=Roboto:wght@400;700&family=Ubuntu:wght@400;500&display=swap">
<style>
  :root {
    --green-deep: #118b44;
    --green-light: #5cbf3a;
    --green-heading: #6cc040;
    --text-body: #454545;
    --band-gray: #d6d6d6;
    --faint: #f3f3f3;
    --white: #ffffff;
  }
  * { margin: 0; padding: 0; box-sizing: border-box; }
  html, body { width: 1200px; height: 900px; overflow: hidden; background: var(--white); }
  .slide { position: relative; width: 1200px; height: 900px; overflow: hidden; background: var(--white); }

  .header-band {
    position: absolute; left: 0; top: 0; width: 1200px; height: 87px;
    background: var(--green-deep);
  }
  .header-rule {
    position: absolute; left: 0; top: 90px; width: 1200px; height: 3px;
    background: var(--green-light);
  }
  .slide-title {
    position: absolute; left: 27px; top: 20px;
    font-family: "Ubuntu", sans-serif; font-weight: 400; font-size: 36px;
    color: var(--white); letter-spacing: 0.5px;
  }
  .brand {
    position: absolute; right: 10px; top: 26px;
    display: flex; align-items: center; gap: 8px;
    font-family: "Ubuntu", sans-serif; font-weight: 400; font-size: 22px;
    color: var(--white);
  }
  .brand-dot { width: 12px; height: 12px; border-radius: 50%; background: var(--white); }

  .backdrop-art {
    position: absolute; left: 720px; top: 135px; width: 465px; height: 705px;
    background: radial-gradient(ellipse at 55% 50%, var(--faint) 0%, rgba(243,243,243,0.6) 45%, rgba(255,255,255,0) 75%);
  }

  .content { position: absolute; left: 0; top: 0; width: 1200px; }
  .item { position: absolute; left: 0; width: 1200px; }
  .item-marker {
    position: absolute; left: 48px; top: 6px;
    width: 16px; height: 16px; border-radius: 50%; background: var(--green-deep);
  }
  .item-heading {
    position: absolute; left: 97px; top: 0;
    font-family: "Roboto", sans-serif; font-weight: 700; font-size: 24px; line-height: 28px;
    color: var(--green-heading); white-space: nowrap;
  }
  .item-body {
    position: absolute; left: 100px; top: 32px;
    font-family: "Roboto", sans-serif; font-weight: 400; font-size: 18px; line-height: 30px;
    color: var(--text-body); white-space: pre;
  }
  .item-body span { display: block; }

  .footer-band {
    position: absolute; left: 0; bottom: 0; width: 1200px; height: 24px;
    background: var(--band-gray);
  }
</style>
</head>
<body>
<div class="slide">
  <div class="header-band"></div>
  <div class="header-rule"></div>
  <h1 class="slide-title">Project Title Here</h1>
  <div class="brand"><span class="brand-dot"></span><span>Vast KELP</span></div>

  <div class="backdrop-art" role="img" aria-label="Faint molecular connection pattern in light gray"></div>

  <div class="content">
    <section class="item" style="top:156px">
      <span class="item-marker"></span>
      <h2 class="item-heading">Lorem ipsum dolor sit Lorem ipsum dolor sit  Lorem ipsum dolor sit</h2>
      <p class="item-body"><span>Lorem ipsum dolor sit Lorem ipsum dolor sit  Lorem ipsum dolor sit Lorem ipsum dolor sit  Lorem ipsum dolor sit Lorem ipsum</span><span>dolor sit  Lorem ipsum dolor sit Lorem ipsum dolor sit  Lorem ipsum dolor sit Lorem ipsum dolor sit  Lorem ipsum dolor sit Lorem</span><span>ipsum dolor sit  Lorem ipsum dolor sit Lorem ipsum dolor sit  Lorem ipsum dolor sit Lorem ipsum dolor sit</span></p>
    </section>
    <section class="item" style="top:337px">
      <span class="item-marker"></span>
      <h2 class="item-heading">Lorem ipsum dolor sit Lorem ipsum dolor sit  Lorem ipsum dolor sit</h2>
      <p class="item-body"><span>Lorem ipsum dolor sit Lorem ipsum dolor sit  Lorem ipsum dolor sit Lorem ipsum dolor sit  Lorem ipsum dolor sit Lorem ipsum</span><span>dolor sit  Lorem ipsum dolor sit Lorem ipsum dolor sit  Lorem ipsum dolor sit Lorem ipsum dolor sit  Lorem ipsum dolor sit Lorem</span><span>ipsum dolor sit  Lorem ipsum dolor sit Lorem ipsum dolor sit  Lorem ipsum dolor sit Lorem ipsum dolor sit</span></p>
    </section>
    <section class="item" style="top:518px">
      <span class="item-marker"></span>
      <h2 class="item-heading">Lorem ipsum dolor sit Lorem ipsum dolor sit  Lorem ipsum dolor sit</h2>
      <p class="item-body"><span>Lorem ipsum dolor sit Lorem ipsum dolor sit  Lorem ipsum dolor sit Lorem ipsum dolor sit  Lorem ipsum dolor sit Lorem ipsum</span><span>dolor sit  Lorem ipsum dolor sit Lorem ipsum dolor sit  Lorem ipsum dolor sit Lorem ipsum dolor sit  Lorem ipsum dolor sit Lorem</span><span>ipsum dolor sit  Lorem ipsum dolor sit Lorem ipsum dolor sit  Lorem ipsum dolor sit Lorem ipsum dolor sit</span></p>
    </section>
    <section class="item" style="top:699px">
      <span class="item-marker"></span>
      <h2 class="item-heading">Lorem ipsum dolor sit Lorem ipsum dolor sit  Lorem ipsum dolor sit</h2>
      <p class="item-body"><span>Lorem ipsum dolor sit Lorem ipsum dolor sit  Lorem ipsum dolor sit Lorem ipsum dolor sit  Lorem ipsum dolor sit Lorem ipsum</span><span>dolor sit  Lorem ipsum dolor sit Lorem ipsum dolor sit  Lorem ipsum dolor sit Lorem ipsum dolor sit  Lorem ipsum dolor sit Lorem</span><span>ipsum dolor sit  Lorem ipsum dolor sit Lorem ipsum dolor sit  Lorem ipsum dolor sit Lorem ipsum dolor sit</span></p>
    </section>
  </div>

  <div class="footer-band"></div>
</div>
</body>
</html>
```